11 x 11 Flyer Design for Social Media - Reverse Mortgages

62 or older?

A Reverse Mortgage
could be
Your Road to Financial Freedom

* No Monthly Payments
* No Income Requirements
* No Credit Score Requirements
* No Loss of Ownership

Receive cash by lump sum, monthly installments or a line of credit!!

Call us today for a Free Consultation!!
(800) 471-2965

Bluegate Financial Services, Inc.
NMLS #318760
www.bluegatehome.com

```html
<!DOCTYPE html>
<html lang="en">
<head>
<meta charset="utf-8">
<title>Reverse Mortgage Flyer</title>
<link href="https://fonts.googleapis.com/css2?family=Montserrat:wght@600;700;800&family=Roboto:wght@500;700&display=swap" rel="stylesheet">
<style>
  :root {
    --brand-blue: #0760a6;
    --deep-blue: #1a5ea8;
    --gold: #a89a2a;
    --white: #ffffff;
    --ink: #222222;
    --muted: #5a5a5a;
    --sky: #e9eef0;
    --sea: #c9d3d6;
  }
  * { margin: 0; padding: 0; box-sizing: border-box; }
  html, body { width: 1200px; height: 1200px; overflow: hidden; background: var(--white); }
  .flyer { position: relative; width: 1200px; height: 1200px; background: var(--white); font-family: "Montserrat", sans-serif; }
  .photo {
    position: absolute; left: 400px; top: 0; width: 800px; height: 706px;
    background: linear-gradient(90deg, rgba(255,255,255,1) 0%, var(--sky) 25%, var(--sea) 60%, #d8dcd8 100%);
  }
  .brand {
    position: absolute; left: 40px; top: 110px; display: flex; align-items: center; gap: 16px;
    color: var(--brand-blue); font-weight: 700; font-size: 30px;
  }
  .brand-dot { width: 34px; height: 34px; border-radius: 50%; background: var(--gold); flex: none; }
  .shapes { position: absolute; inset: 0; }
  .headline { position: absolute; left: 34px; top: 310px; color: var(--white); line-height: 1; }
  .headline .age { font-size: 116px; font-weight: 800; display: block; height: 105px; }
  .headline .age span { font-weight: 600; }
  .headline .older { font-size: 118px; font-weight: 800; display: block; margin-top: -4px; }
  .rule { position: absolute; left: 39px; top: 540px; width: 408px; height: 3px; background: var(--white); }
  .subhead { position: absolute; left: 38px; top: 560px; color: var(--white); font-weight: 700; letter-spacing: 1px; }
  .subhead .line { display: block; font-size: 39px; line-height: 45px; }
  .subhead .line.strong { font-size: 49px; line-height: 58px; letter-spacing: 0.5px; }
  .site { position: absolute; left: 722px; top: 652px; font-size: 34px; font-weight: 700; color: var(--ink); letter-spacing: 0.5px; }
  .benefits { position: absolute; top: 756px; left: 0; width: 1200px; }
  .benefit { position: absolute; width: 260px; text-align: center; font-family: "Roboto", sans-serif; font-weight: 500; font-size: 26px; line-height: 28px; color: var(--muted); }
  .benefit svg { display: block; margin: 0 auto 14px; }
  .offer { position: absolute; top: 932px; width: 1200px; text-align: center; font-family: "Roboto", sans-serif; font-weight: 700; font-size: 55px; line-height: 58px; color: var(--deep-blue); }
  .cta { position: absolute; left: 44px; top: 1068px; width: 1112px; height: 58px; border-radius: 10px; background: var(--gold); overflow: hidden; display: flex; }
  .cta-label { width: 756px; background: var(--brand-blue); border-radius: 10px 0 0 10px; color: var(--white); font-weight: 700; font-size: 34px; line-height: 58px; padding-left: 30px; letter-spacing: 0.5px; }
  .cta-phone { flex: 1; color: var(--white); font-weight: 700; font-size: 38px; line-height: 58px; padding-left: 20px; letter-spacing: 1px; }
  .footer { position: absolute; top: 1140px; width: 1200px; text-align: center; font-weight: 700; font-size: 25px; color: var(--ink); letter-spacing: 0.5px; }
  .footer .sep { font-weight: 400; color: #999; margin: 0 12px; }
</style>
</head>
<body>
<main class="flyer">
  <div class="photo" role="img" aria-label="Photo of a smiling senior couple in white clothing on a beach"></div>

  <div class="brand"><span class="brand-dot"></span>Bluegate Financial Services, Inc.</div>

  <svg class="shapes" width="1200" height="1200" viewBox="0 0 1200 1200" aria-hidden="true">
    <polygon points="0,287 401,287 418,304 0,304" fill="var(--gold)"/>
    <polygon points="0,304 523,304 634,718 0,718" fill="var(--brand-blue)"/>
    <polygon points="636,706 1200,706 1200,719 624,719" fill="var(--gold)"/>
  </svg>

  <h1 class="headline">
    <span class="age">62 <span>or</span></span>
    <span class="older">Older?</span>
  </h1>
  <div class="rule"></div>
  <p class="subhead">
    <span class="line">A Reverse Mortgage</span>
    <span class="line">could be Your Road to</span>
    <span class="line strong">Financial Freedom</span>
  </p>
  <div class="site">www.bluegatehome.com</div>

  <section class="benefits">
    <div class="benefit" style="left:6px">
      <svg width="72" height="72" viewBox="0 0 72 72"><circle cx="36" cy="36" r="36" fill="var(--brand-blue)"/><circle cx="28" cy="38" r="11" fill="none" stroke="#fff" stroke-width="3"/><text x="28" y="44" font-size="15" font-weight="700" fill="#fff" text-anchor="middle" font-family="Roboto, sans-serif">$</text><rect x="40" y="28" width="16" height="5" rx="2" fill="#fff"/><rect x="40" y="35" width="16" height="5" rx="2" fill="#fff"/><rect x="40" y="42" width="16" height="5" rx="2" fill="#fff"/></svg>
      No Monthly<br>Payments
    </div>
    <div class="benefit" style="left:298px">
      <svg width="72" height="72" viewBox="0 0 72 72"><circle cx="36" cy="36" r="36" fill="var(--brand-blue)"/><rect x="23" y="20" width="24" height="32" rx="2" fill="#fff"/><rect x="27" y="27" width="4" height="3" fill="var(--brand-blue)"/><rect x="27" y="34" width="4" height="3" fill="var(--brand-blue)"/><rect x="27" y="41" width="4" height="3" fill="var(--brand-blue)"/><line x1="36" y1="42" x2="50" y2="24" stroke="#fff" stroke-width="4"/></svg>
      No Income<br>Requirements
    </div>
    <div class="benefit" style="left:620px">
      <svg width="72" height="72" viewBox="0 0 72 72"><circle cx="36" cy="36" r="36" fill="var(--brand-blue)"/><rect x="20" y="30" width="32" height="18" rx="2" fill="none" stroke="#fff" stroke-width="3"/><rect x="25" y="36" width="5" height="6" fill="#fff"/><rect x="33" y="36" width="5" height="6" fill="#fff"/><rect x="41" y="36" width="5" height="6" fill="#fff"/><circle cx="27" cy="23" r="3" fill="#fff"/><circle cx="36" cy="21" r="3" fill="#fff"/><circle cx="45" cy="23" r="3" fill="#fff"/></svg>
      No Credit Score<br>Requirements
    </div>
    <div class="benefit" style="left:918px">
      <svg width="72" height="72" viewBox="0 0 72 72"><circle cx="36" cy="36" r="36" fill="var(--brand-blue)"/><circle cx="32" cy="24" r="7" fill="#fff"/><path d="M18 54 Q18 36 32 36 Q46 36 46 54 Z" fill="#fff"/><circle cx="46" cy="40" r="8" fill="var(--brand-blue)" stroke="#fff" stroke-width="2.5"/><text x="46" y="45" font-size="12" font-weight="700" fill="#fff" text-anchor="middle" font-family="Roboto, sans-serif">$</text></svg>
      No Loss of<br>Ownership
    </div>
  </section>

  <p class="offer">Receive cash by lump sum<br>monthly installments or a line of credit!!</p>

  <div class="cta">
    <div class="cta-label">Call us today for a Free Consultation!!</div>
    <div class="cta-phone">(800) 471-2965</div>
  </div>

  <p class="footer">Bluegate Financial Services, Inc.<span class="sep">|</span>NMLS #318760</p>
</main>
</body>
</html>
```